Business Cards Design for the electrical wholesaler: clean bold dynamic :)

We need a business card design that would follow our latest brand guidelines. As an electrical wholesaler we want to bring a fresh look and feel into the industry. The design should be clean bold and dynamic. It should come alive with the renewed energy of our green colour. Our grey colour should keep things balanced and complement the notion of maturity and responsibility. We employ Lato as a corporate font however are not bound by this font and we’re open to interpretation here.

Target Market(s)

Electrical contractors

Industry/Entity Type

Business

Contact Information for Business Card

Logo
Name & Surname: Olena Dovbush
Job Title: Director of Marketing
Email: helen.dovbush@mailvane.example
Cell phone: XXX.XXX.XXXX
Address: 20917 - 87 Ave. Edmonton, AB, Canada. T6K 2R8
Business Phone: 780.555.0187
Website: www.qorvil.example

Font styles to use
Other font styles liked:
• Lato

Requirements
Must have
• Logo & website
Nice to have
• Brand elements - some of them you may find in the attached Brand Guidelines (e.g. three lines on the background signifying "W")

```html
<!DOCTYPE html>
<html lang="en">
<head>
<meta charset="utf-8">
<title>Qorvil Business Cards</title>
<link href="https://fonts.googleapis.com/css2?family=Lato:wght@400;700&display=swap" rel="stylesheet">
<style>
  :root {
    --bg-left: #4f7191;
    --bg-right: #233f62;
    --card: #ffffff;
    --grey: #4d4d4f;
    --grey-soft: #6a6a6c;
    --green: #8cc63f;
    --rule: #7a7a7a;
  }
  * { box-sizing: border-box; margin: 0; padding: 0; }
  html, body { width: 1200px; height: 1000px; overflow: hidden; }
  body {
    position: relative;
    font-family: "Lato", Arial, sans-serif;
    color: var(--grey);
    background: linear-gradient(90deg, var(--bg-left) 0 598px, var(--bg-right) 598px 100%);
  }
  .card {
    position: absolute;
    background: var(--card);
  }
  .card--rounded { border-radius: 30px; }
  .card--front-rounded { left: 64px; top: 60px; width: 508px; height: 290px; }
  .card--back-rounded { left: 64px; top: 427px; width: 508px; height: 289px; }
  .card--front-square { left: 624px; top: 283px; width: 514px; height: 293px; }
  .card--back-square { left: 624px; top: 639px; width: 513px; height: 294px; }

  .brand {
    display: flex;
    align-items: center;
    gap: 12px;
    font-weight: 700;
    color: var(--grey);
    line-height: 1;
  }
  .brand__mark { background: var(--green); flex: none; }
  .card--front .brand {
    position: absolute;
    left: 50%; top: 50%;
    transform: translate(-50%, -50%);
    font-size: 64px;
  }
  .card--front .brand__mark { width: 46px; height: 46px; }
  .card--back .brand {
    position: absolute;
    right: 30px; top: 28px;
    font-size: 42px;
  }
  .card--back .brand__mark { width: 30px; height: 30px; }

  .contact__name {
    position: absolute; right: 30px; top: 94px;
    font-size: 26px; font-weight: 400;
  }
  .contact__title {
    position: absolute; right: 30px; top: 130px;
    font-size: 15px; color: var(--grey-soft);
  }
  .contact__rule {
    position: absolute; left: 27px; top: 142px;
    width: 289px; border-top: 1px solid var(--rule);
  }
  .contact__address {
    position: absolute; left: 27px; top: 155px;
    font-size: 15px; line-height: 19px; color: var(--grey-soft);
    padding-left: 20px;
  }
  .contact__address svg { position: absolute; left: 0; top: 2px; }
  .contact__lines {
    position: absolute; right: 30px; top: 178px;
    list-style: none; text-align: right;
    font-size: 17px; line-height: 24px;
  }
  .contact__lines li { display: flex; align-items: center; justify-content: flex-end; gap: 14px; }
  .contact__lines svg { width: 14px; height: 14px; flex: none; }
  .contact__web {
    position: absolute; left: 27px; bottom: 28px;
    font-size: 14px; color: var(--grey-soft);
  }
  .icon { fill: var(--grey); }
</style>
</head>
<body>

  <section class="card card--rounded card--front card--front-rounded">
    <div class="brand"><span class="brand__mark"></span>qorvil</div>
  </section>

  <section class="card card--rounded card--back card--back-rounded">
    <div class="brand"><span class="brand__mark"></span>qorvil</div>
    <h2 class="contact__name">Olena Dovbush</h2>
    <p class="contact__title">Director of Marketing</p>
    <div class="contact__rule"></div>
    <p class="contact__address">
      <svg width="10" height="14" viewBox="0 0 10 14"><path class="icon" d="M5 0C2.2 0 0 2.2 0 5c0 3.6 5 9 5 9s5-5.4 5-9c0-2.8-2.2-5-5-5zm0 7a2 2 0 1 1 0-4 2 2 0 0 1 0 4z"/></svg>
      20917 - 87 Ave. Edmonton<br>AB, Canada. T6K 2R8
    </p>
    <ul class="contact__lines">
      <li>780.555.0187 <svg viewBox="0 0 14 14"><path class="icon" d="M3 1l2.5 3-1.5 1.5c.8 1.8 2.2 3.2 4 4L9.5 8 13 10.5 11.5 13C6 12.5 1.5 8 1 2.5z"/></svg></li>
      <li>780.555.0187 <svg viewBox="0 0 14 14"><path class="icon" d="M1 5c0-2 3-3 6-3s6 1 6 3v1h-3V5H4v1H1zm2 2h8l1 5H2zm4 1.5a1.5 1.5 0 1 0 0 3 1.5 1.5 0 0 0 0-3z"/></svg></li>
      <li>helen.dovbush@mailvane.example <svg viewBox="0 0 14 14"><path class="icon" d="M1 3h12v8H1zm1 1v.5l5 3 5-3V4z"/></svg></li>
    </ul>
    <p class="contact__web">www.qorvil.example</p>
  </section>

  <section class="card card--front card--front-square">
    <div class="brand"><span class="brand__mark"></span>qorvil</div>
  </section>

  <section class="card card--back card--back-square">
    <div class="brand"><span class="brand__mark"></span>qorvil</div>
    <h2 class="contact__name">Olena Dovbush</h2>
    <p class="contact__title">Director of Marketing</p>
    <div class="contact__rule"></div>
    <p class="contact__address">
      <svg width="10" height="14" viewBox="0 0 10 14"><path class="icon" d="M5 0C2.2 0 0 2.2 0 5c0 3.6 5 9 5 9s5-5.4 5-9c0-2.8-2.2-5-5-5zm0 7a2 2 0 1 1 0-4 2 2 0 0 1 0 4z"/></svg>
      20917 - 87 Ave. Edmonton<br>AB, Canada. T6K 2R8
    </p>
    <ul class="contact__lines">
      <li>780.555.0187 <svg viewBox="0 0 14 14"><path class="icon" d="M3 1l2.5 3-1.5 1.5c.8 1.8 2.2 3.2 4 4L9.5 8 13 10.5 11.5 13C6 12.5 1.5 8 1 2.5z"/></svg></li>
      <li>780.555.0187 <svg viewBox="0 0 14 14"><path class="icon" d="M1 5c0-2 3-3 6-3s6 1 6 3v1h-3V5H4v1H1zm2 2h8l1 5H2zm4 1.5a1.5 1.5 0 1 0 0 3 1.5 1.5 0 0 0 0-3z"/></svg></li>
      <li>helen.dovbush@mailvane.example <svg viewBox="0 0 14 14"><path class="icon" d="M1 3h12v8H1zm1 1v.5l5 3 5-3V4z"/></svg></li>
    </ul>
    <p class="contact__web">www.qorvil.example</p>
  </section>

</body>
</html>
```